Design A Beginners Ketogenic Recipe Book Cover

I'm looking for a recipe book cover that looks professional, and incoporates "The Sunday Harvest Table Cookbook". I have plenty more recipe photos if needed, but would love a pro's take on the graphic design.

Its targeted at beginners of the ketogenic diet, and I would like it to highlight a similar design from my website and graphics found at https://www.brightmeadowhub.com.au/

Target Market(s)

American / Australian / Canadian Females - Ages from 35 - 50. Interested in weight loss, diets, ketogenic diet.

Industry/Entity Type

Cooking

Font styles to use
Serif

Colors
33a6d7
0692cd
85cae6
cee9f5

Requirements
Must have
• Must include my logo, must include title "The Sunday Harvest Table Cookbook"
Nice to have
• I don't have a strong idea for the cook book, but If you reseach cookbooks you'll get a good idea on what a cookbook should look like.

```html
<!DOCTYPE html>
<html lang="en">
<head>
<meta charset="utf-8">
<title>The Sunday Harvest Table Cookbook — Cover</title>
<link rel="stylesheet" href="https://fonts.googleapis.com/css2?family=Oleo+Script&family=Oswald:wght@600&display=swap">
<style>
  :root {
    --stage: #e6e6e6;
    --paper: #ffffff;
    --brand-blue: #1a87c0;
    --brand-sky: #33a6d7;
    --script-brown: #4a2418;
    --bread: #dcc197;
    --bread-deep: #c99a5e;
    --aqua: #8fe6ee;
    --aqua-deep: #7fc9b8;
    --almond-blue: #5ab8d6;
    --almond-deep: #3f8fae;
    --cookie: #c9a170;
    --cookie-deep: #7a5a3c;
  }
  * { box-sizing: border-box; margin: 0; padding: 0; }
  html, body { width: 1200px; height: 960px; overflow: hidden; }
  body { background: var(--stage); position: relative; }

  .cover {
    position: absolute;
    left: 300px; top: 30px;
    width: 601px; height: 900px;
    background: var(--paper);
    box-shadow: 0 6px 18px rgba(0,0,0,0.18);
    overflow: hidden;
  }
  .photo { position: absolute; }
  .photo--bread {
    left: 0; top: 0; width: 291px; height: 441px;
    background: linear-gradient(160deg, #f1dcb8 0%, var(--bread) 55%, var(--bread-deep) 100%);
  }
  .photo--cookie-stack {
    left: 311px; top: 0; width: 290px; height: 441px;
    background: linear-gradient(180deg, var(--aqua) 0%, var(--aqua) 25%, var(--aqua-deep) 60%, #5f8a74 100%);
  }
  .photo--almonds {
    left: 0; top: 459px; width: 291px; height: 441px;
    background: linear-gradient(175deg, #7fb7b4 0%, var(--almond-blue) 30%, var(--almond-deep) 100%);
  }
  .photo--cookies-plate {
    left: 311px; top: 459px; width: 290px; height: 441px;
    background: linear-gradient(180deg, #b8935f 0%, var(--cookie) 45%, #8a7258 80%, #4c4a48 100%);
  }

  .title-panel {
    position: absolute;
    left: 110px; top: 292px;
    width: 381px; height: 316px;
    background: var(--paper);
    text-align: center;
  }
  .brand {
    position: absolute;
    left: 138px; top: 17px;
    display: flex; align-items: center; gap: 6px;
  }
  .brand__mark {
    width: 48px; height: 48px;
    background: var(--brand-sky);
  }
  .brand__name {
    font-family: "Oswald", sans-serif;
    font-weight: 600;
    font-size: 15px;
    line-height: 17px;
    color: var(--brand-sky);
    text-align: left;
    text-transform: uppercase;
  }
  .title__script {
    position: absolute;
    left: 0; right: 0; top: 86px;
    font-family: "Oleo Script", cursive;
    font-size: 38px;
    color: var(--script-brown);
    line-height: 1;
  }
  .title__main {
    position: absolute;
    left: 0; right: 0; top: 134px;
    font-family: "Oswald", sans-serif;
    font-weight: 600;
    font-size: 80px;
    line-height: 0.95;
    letter-spacing: -1px;
    color: var(--brand-blue);
    text-transform: uppercase;
  }
</style>
</head>
<body>
  <main class="cover">
    <div class="photo photo--bread" role="img" aria-label="Close-up of a sliced loaf of golden low-carb bread"></div>
    <div class="photo photo--cookie-stack" role="img" aria-label="Stack of chocolate chip cookies against an aqua background"></div>
    <div class="photo photo--almonds" role="img" aria-label="Whole almonds scattered on a blue surface"></div>
    <div class="photo photo--cookies-plate" role="img" aria-label="Golden chocolate chip cookies stacked on a dark plate"></div>

    <section class="title-panel">
      <div class="brand">
        <span class="brand__mark"></span>
        <span class="brand__name">Bright<br>Meadow<br>Hub</span>
      </div>
      <h1>
        <span class="title__script">The Sunday Harvest</span>
        <span class="title__main">Table<br>Cookbook</span>
      </h1>
    </section>
  </main>
</body>
</html>
```